■ 依頼の目的/概要
グループ企業内で使用する、業務支援ポータルサイトのリニューアルです。
依頼内容は、TOPページのデザイン作成です。
レイアウト案が2パターンありますので、制作要項をもとに、合計2パターンご提案をお願いします。
(制作要項:P3~4参照)

■現在の参考サイト
制作要項に、参考URLを掲載しております。詳しくは添付の制作要項を参照ください。

■現状の課題
・デザインが洗練されていない。
・情報を伝達、共有するツールとしては分かり難いレイアウトの為、社員に情報が伝わりにくい。
・メニューが煩雑になっており、従業員が必要な情報を探すときにも、目的にたどり着きにくい。

■ 重視する点/検討基準
① デザイン性(使いやすさ・見やすさ・親しみやすさ)
② 納期厳守

■ 具体的な制作数
TOPページ:2パターン(デザイン) *制作要項:P.3~4参照

■募集条件
キャラクターにつきましては、商標上の問題により、現在開示することが出来ないため、
アタリで作成をお願い致します。
デザイン選定後、当選者にキャラクターデザインをお渡ししますので、
差し込んで頂き、納品完了となります。
ご認識をお願いします。

■納品ファイル
・イラストレーター形式(.ai)
・フォトショップ形式(.psd)
*1 募集条件を満たした状態のデザイン
*2 納品のフォトショップは、できるだけレイヤー結合せず、コーディング時に部品として
扱えるようにしてください。こちらでも再加工できる状態でお願いします。

■選考の進め方
ご提案頂いたデザイン内容・コンセプトなどをもとに、プロジェクトメンバーで選考、決定致します。

皆様からの、素晴らしいご提案を、お待ちしております。
宜しくお願い致します。
この度、募集期間を5日間、延長させて頂きます。
また、依頼金額についても 50,000円 ⇒ 70,000円 に変更致します。

今一度、ご提案を頂ければ幸甚です。引き続き、よろしくお願いします。
こちらが要望するデザインイメージと、使用していただくデザインパーツを加えております。
改めて、ご参照頂ますよう、お願いします。
コンセプトに見合うデザインは、ご提案頂いておりますが、あと1日延長させて頂きます。
引き続き、皆様からのご提案をお待ちしております。
宜しくお願い致します。
たくさんのご提案ありがとうございます。
もうすこしパターンを見てみたいため、3日間延長いたします。

宜しくお願い致します。
度々申し訳御座いません。
幾つか、イメージに則したデザインをご提案頂いておりますが、
提案数が少ないので、再度延長致します。

見ていて楽しくなるようなポータルサイトデザインのご提案をお待ちしております。
引き続き宜しくお願い致します。
度々の延長により、ご迷惑をおかけしております。
今回、デザインについて、様々なパターンから検討したかったのですが、
思うように提案が集まらなかった為、依頼金額の追加、
及び期間の延長を行なっております。

情報不足により、皆様のデザインスキルを引き出すことができなかったと思い、
今回、募集要項に、開示できる限りの情報を添えて、更新しております。
ご参照頂ければ幸いです。

皆様からの素晴らしい提案をお待ちしております。
お世話になっております。
度々、申し訳ございませんが、1週間延長致します。
開示可能な情報が少ない為、提案するに出来ない状況なのでは無いかと
思いますが、必要な情報や、ご質問等御座いましたら、お気軽にお申し
付けください。

宜しくお願い致します。
度々申し訳御座いません。
再度1週間延長します。
素晴らしい提案を頂いておりますが、採用にまでは至っていない状況です。

ポータルサイトの用途を伝えきれていないかもしれませんので、
基本機能を、以下に明示します。

①サービス窓口のオペレータが、お客様へ案内する際に活用できるサービス情報データベース
②研修担当者が新人教育・研修時に活用できるマニュアル等の教育支援ツール
③新人社員が、空いた時間にテストやマニュアルなどを活用できる自己学習支援ツール
④目標などの数値関連を開示し、他のオペレータとの競争環境をつくり上げる、目標支援ツール
⑤対応時に手本となる音声データや対応時の良い台本などが拝聴・閲覧ができるスキルアップ支援ツール
⑥オペレータが業務において、疑問点や不明点、改善提案などを行い、実際にサービス運営陣も回答ができるFAQツール

上記の6点を利用でき、アクセス数を伸ばせるような、クオリティの高いポータルサイトデザインを募集致します。

ご質問のある方は、メッセージにて個別に回答致しますので、お気軽にお申し付けください。

引き続き、宜しくお願い致します。
本依頼に対しまして、お忙しい中、数々のデザインをご提案頂き、
誠にありがとうございました。
皆様からご提案頂いた貴重なデザイン案は、現在こちらで検討させて
頂いております。

今回の依頼は、スタート時点から、具体的な完成形が見えにくい依頼と
なっており、募集期限が大幅に伸び、Toviraの皆様方にはご迷惑をお掛け
致しました。
申し訳ございませんでした。

つきましては、完成形により具体性を持たせるため、弊社でデザインイメージを
作成致しました。
お手数をお掛けしますが、修正箇所は添付ファイルのデザインイメージ下部に
記載しておりますので、ご確認をお願い致します。

また、恐れ入りますが、依頼期限は12/28(金)まで、延長させて頂きたいと
思います。
素敵なデザイン案を、ご検討頂けますと幸甚です。

宜しくお願い申し上げます。

こちらの要望した、楽しげで、飽きの来ないデザインに加え、
ピンクを基調としたサイトカラーと、フェルト調のデザインパーツが
マッチしており、細部にこだわりを感じられるデザインになっていました。

まず、今回の依頼について、こちらの要望がうまく定まらず、ご迷惑をお掛けしたこと、お詫び申し上げます。
また、度重なる延長にも関わらず、ご協力頂きましたトヴィラの皆さまに感謝致します。誠にありがとうございました。

今後も、Tovirasを通して仕事を依頼する機会があるかと思いますが、その際はまた、素晴らしいご提案を頂ければ幸甚でございます。

```html
<!DOCTYPE html>
<html lang="ja">
<head>
<meta charset="utf-8">
<title>SAMPLE PORTAL</title>
<link href="https://fonts.googleapis.com/css2?family=Noto+Sans+JP:wght@400;700;900&display=swap" rel="stylesheet">
<style>
:root{
  --lime:#cadd0a;
  --lime-light:#e9f29a;
  --lime-pale:#f6f9d8;
  --green-dark:#3f6a12;
  --green:#6a9a1c;
  --red:#e2382a;
  --orange:#ef8a1b;
  --ink:#333;
  --mute:#777;
  --line:#d6d6d6;
  --panel:#f4f4f4;
  --footer:#e6e6e6;
  --footer-dark:#3a3a3a;
}
*{box-sizing:border-box;margin:0;padding:0}
html,body{width:820px;height:1200px;overflow:hidden}
body{font-family:"Noto Sans JP",sans-serif;color:var(--ink);background:#fff;font-size:11px;position:relative}
ul{list-style:none}

.site-header{height:58px;padding:10px 20px 0;display:flex;justify-content:space-between}
.brand-name{font-size:22px;font-weight:900;letter-spacing:1px;line-height:1}
.brand-sub{font-size:8px;color:var(--mute);margin-top:4px}
.search{display:flex;gap:4px;margin-top:6px}
.search-field{width:170px;height:22px;border:1px solid #bbb;background:#fff}
.search-btn{width:44px;height:22px;background:var(--footer-dark);color:#fff;font-size:10px;display:flex;align-items:center;justify-content:center}

.global-nav{height:26px;background:var(--lime);display:flex;padding:0 20px;border-bottom:2px solid var(--green)}
.global-nav li{flex:1;text-align:center;line-height:26px;font-size:11px;font-weight:700;color:#fff;border-right:1px solid rgba(255,255,255,.6)}
.global-nav li.current{background:var(--green)}

.hero{height:164px;background:linear-gradient(#e1ee6a,var(--lime));display:flex;padding:14px 20px;gap:14px;position:relative}
.hero-notice{width:360px;position:relative}
.hero-title{background:var(--green-dark);color:#fff;font-size:20px;font-weight:900;padding:8px 14px;border-radius:4px;width:330px}
.hero-subtitle{background:#fff6a0;color:var(--green-dark);font-size:17px;font-weight:900;padding:6px 14px;margin-top:6px;width:260px;border-radius:4px}
.hero-character{position:absolute;left:0;top:104px;width:46px;height:40px;border-radius:8px;background:#9a9a9a}
.hero-caption{position:absolute;left:56px;top:116px;font-size:11px;font-weight:700;color:var(--green-dark);background:#fff;padding:3px 10px;border-radius:10px}
.hero-rules{flex:1;background:#fff;border-radius:6px;padding:10px 14px}
.hero-lead{font-size:15px;font-weight:900;line-height:1.35;text-align:center;color:var(--ink)}
.rule-list{display:grid;grid-template-columns:1fr 1fr;gap:4px;margin-top:8px}
.rule-list li{background:var(--red);color:#fff;font-size:10px;font-weight:700;padding:4px 6px;text-align:center}
.hero-foot{display:flex;justify-content:space-between;align-items:center;margin-top:8px;font-size:10px}
.more-btn{background:var(--red);color:#fff;padding:3px 12px;border-radius:3px;font-weight:700}

.topic-tabs{height:44px;padding:8px 20px;display:flex;gap:5px;align-items:center}
.topic-tabs li{flex:1;height:28px;border:1px solid var(--line);background:var(--panel);font-size:8px;line-height:1.3;display:flex;align-items:center;justify-content:center;text-align:center;color:var(--mute)}
.pager{position:absolute;top:244px;left:50%;transform:translateX(-50%);display:flex;gap:4px}
.pager span{width:6px;height:6px;border-radius:50%;background:#bbb}
.pager span.on{background:var(--green)}

.content{display:flex;gap:12px;padding:4px 20px 0}
.main{width:538px}
.side{flex:1}
.panel-head{display:flex;justify-content:space-between;align-items:center;border-bottom:2px solid var(--lime);padding:4px 2px;font-size:13px;font-weight:700}
.panel-head .mark{display:inline-block;width:10px;height:10px;background:var(--lime);margin-right:6px;vertical-align:-1px}
.back-link{font-size:8px;color:var(--mute)}

.sitemap{background:var(--panel);border:1px solid var(--line);margin-top:6px;padding:8px;display:grid;grid-template-columns:repeat(4,1fr);gap:8px;height:118px}
.sitemap-group h3{font-size:11px;background:#fff;border:1px solid var(--line);padding:3px 6px;margin-bottom:5px}
.sitemap-group li{font-size:10px;padding-left:10px;position:relative;line-height:1.7}
.sitemap-group li::before{content:"";position:absolute;left:1px;top:6px;border:3px solid transparent;border-left:4px solid var(--green)}

.news{margin-top:12px}
.news-list li{display:flex;align-items:center;height:25px;border-bottom:1px dotted var(--line);font-size:10px;gap:8px;padding:0 4px}
.news-date{width:64px;color:var(--mute)}
.tag{width:38px;text-align:center;color:#fff;font-size:8px;padding:2px 0;border-radius:2px}
.tag.red{background:var(--red)}.tag.green{background:var(--green)}.tag.orange{background:var(--orange)}
.news-title{flex:1}

.maint{margin-top:12px}

.ranking{border:1px solid var(--line);margin-top:0}
.ranking .panel-head{background:var(--lime-pale)}
.rank-list li{display:flex;align-items:center;gap:8px;padding:3px 10px;border-bottom:1px dotted var(--line);font-size:10px}
.rank-no{width:16px;height:16px;border-radius:50%;background:#bbb;color:#fff;font-size:9px;display:flex;align-items:center;justify-content:center}
.rank-list li.top{font-size:16px;font-weight:700;padding:6px 10px}
.rank-list li.top .rank-no{background:var(--red);width:20px;height:20px;font-size:10px}

.bookmarks{border:1px solid var(--line);margin-top:12px}
.bookmarks .panel-head{background:var(--lime-pale)}
.bookmark-list{padding:6px 8px}
.bookmark-list li{font-size:10px;padding:3px 6px;border-left:4px solid var(--green);background:var(--panel);margin-bottom:4px}
.edit-btn{margin:2px 8px 8px auto;width:70px;text-align:center;background:var(--footer-dark);color:#fff;font-size:9px;padding:3px 0;border-radius:2px}

.pagetop{position:absolute;right:20px;top:924px;background:var(--footer-dark);color:#fff;font-size:8px;padding:2px 8px}
.site-footer{position:absolute;left:0;right:0;top:940px;height:210px;background:var(--footer);border-top:4px solid var(--lime);display:flex;justify-content:center;gap:60px;padding-top:20px}
.footer-group h4{font-size:11px;margin-bottom:6px}
.footer-group li{font-size:10px;line-height:1.9;padding-left:10px;position:relative}
.footer-group li::before{content:"・";position:absolute;left:0}
.copyright{position:absolute;left:0;right:0;top:1150px;height:50px;background:var(--footer-dark);color:#ccc;font-size:9px;text-align:center;line-height:50px}
</style>
</head>
<body>
<header class="site-header">
  <div class="brand">
    <div class="brand-name">SAMPLE PORTAL</div>
    <div class="brand-sub">業務連絡の円滑化と情報共有のための社内ポータルサイト</div>
  </div>
  <div class="search"><div class="search-field"></div><div class="search-btn">検索</div></div>
</header>

<nav>
  <ul class="global-nav">
    <li class="current">トップページ</li><li>学習メニュー</li><li>機能を使う</li><li>業務用印</li><li>日報・成績</li><li>お問合せ</li>
  </ul>
</nav>

<section class="hero">
  <div class="hero-notice">
    <div class="hero-title">業務連絡の効率化について</div>
    <div class="hero-subtitle">(メールの件名の統一化)</div>
    <div class="hero-character" role="img" aria-label="キャラクター(アタリ)"></div>
    <div class="hero-caption">運営事務局からのお知らせです。</div>
  </div>
  <div class="hero-rules">
    <p class="hero-lead">社内の業務効率を図るため、<br>メールの件名をルール化致します。</p>
    <ul class="rule-list">
      <li>1.規格等の場合は【規格】</li><li>2.経費精算の場合は【経費】</li>
      <li>3.業務連絡の場合は【業務】</li><li>4.至急の場合は【至急】</li>
    </ul>
    <div class="hero-foot"><span>ご協力の程、宜しくお願い致します。</span><span class="more-btn">詳しく見る</span></div>
  </div>
</section>

<ul class="topic-tabs">
  <li>業務連絡の場合<br>について</li><li>日報提出の場合<br>について</li><li>経費精算の場合<br>について</li><li>研修受講の場合<br>について</li>
  <li>休暇申請の場合<br>について</li><li>備品申請の場合<br>について</li><li>会議予約の場合<br>について</li><li>出張申請の場合<br>について</li>
</ul>
<div class="pager"><span class="on"></span><span></span><span></span></div>

<div class="content">
  <main class="main">
    <section>
      <div class="panel-head"><span><span class="mark"></span>業務サイトマップ</span></div>
      <div class="sitemap">
        <div class="sitemap-group"><h3>通達を調べる</h3><ul><li>新着通達</li><li>料金表</li><li>サービス一覧</li></ul></div>
        <div class="sitemap-group"><h3>学習する</h3><ul><li>学習ページ</li><li>対応フロー集</li><li>研修テスト</li></ul></div>
        <div class="sitemap-group"><h3>機能を使う</h3><ul><li>メッセージ</li><li>ファイル共有</li><li>マイページ</li></ul></div>
        <div class="sitemap-group"><h3>今日の成績</h3><ul><li>日報</li><li>目標達成率</li><li>ランキング</li></ul></div>
      </div>
    </section>

    <section class="news">
      <div class="panel-head"><span><span class="mark"></span>新着通達</span><span class="back-link">BACK NUMBER ›</span></div>
      <ul class="news-list">
        <li><span class="news-date">2012/11/02</span><span class="news-title">社内連絡用の件名ルール化について通達します。</span><span class="tag red">重要</span></li>
        <li><span class="news-date">2012/11/02</span><span class="news-title">年末年始の窓口営業時間についてのお知らせです。</span><span class="tag green">通達</span></li>
        <li><span class="news-date">2012/11/01</span><span class="news-title">新サービスの料金プランを追加しました。</span><span class="tag orange">更新</span></li>
        <li><span class="news-date">2012/11/01</span><span class="news-title">研修テストの問題を一部改訂しました。</span><span class="tag green">通達</span></li>
        <li><span class="news-date">2012/10/31</span><span class="news-title">対応フロー集の目次を見直しました。</span><span class="tag orange">更新</span></li>
        <li><span class="news-date">2012/10/30</span><span class="news-title">契約変更時の確認事項についての周知です。</span><span class="tag red">重要</span></li>
        <li><span class="news-date">2012/10/29</span><span class="news-title">手続き書類の様式を新しくしました。</span><span class="tag green">通達</span></li>
        <li><span class="news-date">2012/10/26</span><span class="news-title">月間目標の集計方法を変更しました。</span><span class="tag orange">更新</span></li>
        <li><span class="news-date">2012/10/25</span><span class="news-title">FAQに新しい回答を掲載しました。</span><span class="tag green">通達</span></li>
        <li><span class="news-date">2012/10/24</span><span class="news-title">個人情報の取扱い手順について再確認です。</span><span class="tag red">重要</span></li>
      </ul>
    </section>

    <section class="maint">
      <div class="panel-head"><span><span class="mark"></span>障害メンテナンス情報</span><span class="back-link">BACK NUMBER ›</span></div>
      <ul class="news-list">
        <li><span class="news-date">2012/11/01</span><span class="news-title">サーバー定期メンテナンスのお知らせ</span></li>
        <li><span class="news-date">2012/10/28</span><span class="news-title">バックアップ作業に伴う停止について</span></li>
        <li><span class="news-date">2012/10/20</span><span class="news-title">バージョンアップに関するお知らせ</span></li>
      </ul>
    </section>
  </main>

  <aside class="side">
    <section class="ranking">
      <div class="panel-head"><span>今週の検索ワード</span></div>
      <ul class="rank-list">
        <li class="top"><span class="rank-no">1</span>手続き</li>
        <li class="top"><span class="rank-no">2</span>契約</li>
        <li class="top"><span class="rank-no">3</span>料金</li>
        <li><span class="rank-no">4</span>解約</li>
        <li><span class="rank-no">5</span>住所変更</li>
        <li><span class="rank-no">6</span>問合せ</li>
        <li><span class="rank-no">7</span>商品</li>
        <li><span class="rank-no">8</span>請求書</li>
        <li><span class="rank-no">9</span>シリーズ</li>
        <li><span class="rank-no">10</span>支払い</li>
      </ul>
    </section>

    <section class="bookmarks">
      <div class="panel-head"><span>サイト内ブックマーク</span></div>
      <ul class="bookmark-list">
        <li>ブックマークタイトル01</li><li>ブックマークタイトル02</li><li>ブックマークタイトル03</li>
        <li>ブックマークタイトル04</li><li>ブックマークタイトル05</li><li>ブックマークタイトル06</li>
        <li>ブックマークタイトル07</li><li>ブックマークタイトル08</li>
      </ul>
      <div class="edit-btn">編集する</div>
    </section>
  </aside>
</div>

<div class="pagetop">PAGETOP</div>

<footer class="site-footer">
  <div class="footer-group"><h4>学習メニュー</h4><ul><li>学習ページ</li><li>教材リスト</li><li>社内フローマップ</li></ul></div>
  <div class="footer-group"><h4>機能を使う</h4><ul><li>メッセンジャー</li><li>ファイルボックス</li><li>マイページ</li></ul></div>
  <div class="footer-group"><h4>業務用印</h4><ul><li>各種印</li><li>ガイドライン</li><li>押印リスト</li></ul></div>
  <div class="footer-group"><h4>日報・成績</h4><ul><li>日報</li><li>月報</li></ul></div>
</footer>
<div class="copyright">Copyright 2012 SAMPLE PORTAL. All rights reserved.</div>
</body>
</html>
```